Complete Stationary Package for IT Company
Full Stationary (Folder, Envolope, etc) + CD Cover + Background for PC
Complete Stationary Package for IT Company - Information Technology
Marco Vellida
Gerente General
C/Ramon Ferrel #27, Lomas de Vistral, Santo Domingo Este. RD.
marcovellida@qnv.com.do
www.qnv.com.do
marcovellida marcovellida
Hi! Nice work! Could put a QR Code with Contact full Info?
Hi! Please include this text: Aplicaciones * Consultoria * Infraestructura * Soporte

```html
<!DOCTYPE html>
<html lang="es">
<head>
<meta charset="utf-8">
<title>QNV Dominicana – Stationery Package</title>
<link href="https://fonts.googleapis.com/css2?family=Montserrat:wght@700&family=Open+Sans:wght@400;600&display=swap" rel="stylesheet">
<style>
:root{
  --bg:#9a9a9a;
  --frame:#b4b4b4;
  --paper:#ffffff;
  --orange:#f39a1e;
  --teal:#4c6a79;
  --ink:#333333;
  --black:#1b1b1b;
}
*{box-sizing:border-box;margin:0;padding:0}
html,body{width:1200px;height:974px;overflow:hidden}
body{background:var(--bg);font-family:"Open Sans",Arial,sans-serif;color:var(--ink);position:relative}
.frame{position:absolute;left:14px;top:14px;width:1172px;height:946px;border:4px solid var(--frame)}
.piece{position:absolute;background:var(--paper);overflow:hidden;box-shadow:0 2px 5px rgba(0,0,0,.25)}
.swoosh{position:absolute;left:0;bottom:0;width:100%}
.brand{font-family:"Montserrat",Arial,sans-serif;font-weight:700;color:var(--teal);white-space:nowrap;display:flex;align-items:center;gap:.35em;line-height:1}
.brand .dot{width:.55em;height:.55em;border-radius:50%;background:var(--orange);display:inline-block}
.brand.light{color:var(--paper)}
.brand.center{position:absolute;left:0;width:100%;justify-content:center}
.tiny{font-size:6px;line-height:1.45;color:var(--ink)}
.tiny.light{color:#fff}
.addr{position:absolute;text-align:right}
.faint{position:absolute;border-radius:50%;background:var(--orange);opacity:.12}

.card-a{left:74px;top:66px;width:176px;height:97px}
.card-b{left:74px;top:197px;width:176px;height:100px}
.card-c{left:74px;top:334px;width:176px;height:100px;background:var(--teal)}
.letterhead{left:276px;top:66px;width:276px;height:381px}
.slip{left:584px;top:66px;width:140px;height:124px}
.env-a{left:584px;top:224px;width:205px;height:87px}
.env-b{left:584px;top:329px;width:205px;height:92px}
.env-stack{position:absolute;left:847px;top:368px;width:310px;height:224px}
.env-back{position:absolute;left:0;width:310px;height:86px;overflow:hidden;box-shadow:0 2px 5px rgba(0,0,0,.25)}
.env-back.black{top:0;background:var(--black)}
.env-back.orange{top:70px;background:var(--orange)}
.env-back.white{top:138px;background:var(--paper)}
.flap{position:absolute;left:0;top:0;width:100%;height:50px}
.seal{position:absolute;left:150px;top:56px;width:10px;height:10px;border-radius:50%}
.hero-logo{position:absolute;left:905px;top:88px;font-size:26px;color:#fff}
.folder{left:74px;top:492px;width:518px;height:403px}
.folder-edge{position:absolute;left:0;top:0;width:14px;height:100%;background:var(--orange)}
.folder-pocket{position:absolute;left:0;bottom:0;width:100%;height:150px}
.cd{position:absolute;left:618px;top:521px;width:116px;height:116px;border-radius:50%;background:var(--paper);overflow:hidden;box-shadow:0 2px 5px rgba(0,0,0,.3)}
.cd-hole{position:absolute;left:48px;top:48px;width:20px;height:20px;border-radius:50%;background:var(--bg);border:3px solid #ddd}
.sleeve{left:600px;top:640px;width:202px;height:241px}
.fax{left:821px;top:610px;width:310px;height:271px}
.fax h2{position:absolute;left:18px;top:34px;font-family:"Montserrat",Arial,sans-serif;font-size:26px;color:var(--black)}
.fax-grid{position:absolute;left:18px;top:78px;width:272px;display:grid;grid-template-columns:1fr 1fr;column-gap:16px;row-gap:5px;font-size:7px}
.fax-grid span{border-bottom:1px solid #999;padding-bottom:1px}
.fax-checks{position:absolute;left:18px;top:148px;width:272px;display:flex;justify-content:space-between;font-size:6px}
.fax-checks span::before{content:"";display:inline-block;width:5px;height:5px;border:1px solid #666;margin-right:2px;vertical-align:middle}
.fax-rule{position:absolute;left:18px;top:162px;width:272px;border-top:1px solid #999}
</style>
</head>
<body>
<div class="frame"></div>

<div class="piece card-a">
  <div class="brand" style="position:absolute;left:12px;top:10px;font-size:8px">QNV Dominicana</div>
  <div class="tiny" style="position:absolute;left:12px;top:24px">
    <b style="font-size:7px">Marco Vellida</b><br>Gerente General<br>
    C/Ramon Ferrel #27, Lomas de Vistral<br>marcovellida@qnv.com.do<br>www.qnv.com.do
  </div>
  <svg class="swoosh" height="24" viewBox="0 0 100 20" preserveAspectRatio="none"><path d="M0,14 Q50,2 100,6 L100,20 L0,20Z" fill="var(--orange)"/><path d="M0,16 Q50,5 100,9 L100,20 L0,20Z" fill="#fff"/><path d="M0,17 Q55,8 100,11 L100,20 L0,20Z" fill="var(--teal)"/></svg>
</div>

<div class="piece card-b">
  <div class="brand center" style="top:38px;font-size:13px">QNV Dominicana</div>
  <svg class="swoosh" height="26" viewBox="0 0 100 20" preserveAspectRatio="none"><path d="M0,14 Q50,2 100,6 L100,20 L0,20Z" fill="var(--orange)"/><path d="M0,16 Q50,5 100,9 L100,20 L0,20Z" fill="#fff"/><path d="M0,17 Q55,8 100,11 L100,20 L0,20Z" fill="var(--teal)"/></svg>
</div>

<div class="piece card-c">
  <div class="brand light center" style="top:34px;font-size:13px">QNV Dominicana</div>
  <div class="tiny light" style="position:absolute;left:0;width:100%;bottom:12px;text-align:center">www.qnv.com.do</div>
</div>

<div class="piece letterhead">
  <div class="brand" style="position:absolute;left:18px;top:18px;font-size:11px">QNV Dominicana</div>
  <div class="tiny addr" style="right:16px;top:14px">C/Ramon Ferrel #27, Lomas de Vistral<br>Tel. 809-555-0147<br>marcovellida@qnv.com.do</div>
  <div class="faint" style="left:96px;top:112px;width:80px;height:80px"></div>
  <div class="tiny" style="position:absolute;left:0;width:100%;bottom:40px;text-align:center;color:var(--teal)">Aplicaciones * Consultoria * Infraestructura * Soporte</div>
  <svg class="swoosh" height="40" viewBox="0 0 100 20" preserveAspectRatio="none"><path d="M0,6 Q50,14 100,4 L100,20 L0,20Z" fill="var(--orange)"/><path d="M0,9 Q50,16 100,7 L100,20 L0,20Z" fill="#fff"/><path d="M0,20 Q60,14 100,10 L100,20Z" fill="var(--teal)"/></svg>
</div>

<div class="piece slip">
  <div class="brand" style="position:absolute;left:10px;top:12px;font-size:8px">QNV Dominicana</div>
  <div class="tiny" style="position:absolute;left:10px;top:26px">Marco Vellida<br>Gerente General</div>
  <svg class="swoosh" height="18" viewBox="0 0 100 20" preserveAspectRatio="none"><path d="M0,8 Q50,0 100,6 L100,20 L0,20Z" fill="var(--orange)"/><path d="M0,11 Q50,4 100,9 L100,20 L0,20Z" fill="var(--teal)"/></svg>
</div>

<div class="piece env-a">
  <div class="brand" style="position:absolute;left:10px;top:12px;font-size:9px">QNV Dominicana</div>
  <div class="tiny" style="position:absolute;left:84px;top:30px">Marco Vellida<br>C/Ramon Ferrel #27<br>Santo Domingo Este. RD.</div>
  <svg class="swoosh" height="16" viewBox="0 0 100 20" preserveAspectRatio="none"><path d="M0,8 Q50,0 100,6 L100,20 L0,20Z" fill="var(--orange)"/><path d="M0,11 Q50,4 100,9 L100,20 L0,20Z" fill="var(--teal)"/></svg>
</div>

<div class="piece env-b">
  <div class="brand" style="position:absolute;left:10px;top:40px;font-size:10px">QNV Dominicana</div>
  <div class="tiny addr" style="right:10px;top:12px">C/Ramon Ferrel #27<br>Lomas de Vistral</div>
  <svg class="swoosh" height="16" viewBox="0 0 100 20" preserveAspectRatio="none"><path d="M0,8 Q50,0 100,6 L100,20 L0,20Z" fill="var(--orange)"/><path d="M0,11 Q50,4 100,9 L100,20 L0,20Z" fill="var(--teal)"/></svg>
</div>

<div class="brand hero-logo">QNV Dominicana</div>

<div class="env-stack">
  <div class="env-back black"><svg class="flap" viewBox="0 0 100 20" preserveAspectRatio="none"><path d="M0,0 L50,18 L100,0Z" fill="#fff"/></svg><span class="seal" style="background:#fff"></span></div>
  <div class="env-back orange"><svg class="flap" viewBox="0 0 100 20" preserveAspectRatio="none"><path d="M0,0 L50,18 L100,0Z" fill="var(--teal)"/></svg><span class="seal" style="background:#fff"></span></div>
  <div class="env-back white"><svg class="flap" viewBox="0 0 100 20" preserveAspectRatio="none"><path d="M0,0 L50,18 L100,0Z" fill="#e6e6e6"/></svg><span class="seal" style="background:var(--teal)"></span></div>
</div>

<div class="piece folder">
  <div class="folder-edge"></div>
  <div class="faint" style="left:110px;top:100px;width:90px;height:90px"></div>
  <div class="brand" style="position:absolute;left:226px;top:128px;font-size:24px">QNV Dominicana</div>
  <div class="tiny addr" style="right:18px;top:18px">C/Ramon Ferrel #27, Lomas de Vistral<br>Tel. 809-555-0147<br>www.qnv.com.do</div>
  <svg class="folder-pocket" viewBox="0 0 518 150" preserveAspectRatio="none">
    <path d="M0,30 Q260,-10 518,40 L518,150 L0,150Z" fill="var(--orange)"/>
    <path d="M0,38 Q260,2 518,50 L518,150 L0,150Z" fill="#fff"/>
    <path d="M0,90 Q300,30 518,70 L518,150 L0,150Z" fill="var(--teal)"/>
  </svg>
  <div class="brand" style="position:absolute;left:20px;top:296px;font-size:9px">QNV Dominicana</div>
  <div style="position:absolute;left:194px;top:330px;width:72px;height:42px;background:#fff;box-shadow:0 1px 3px rgba(0,0,0,.3)">
    <div class="brand center" style="top:18px;font-size:6px">QNV Dominicana</div>
  </div>
</div>

<div class="cd">
  <div class="brand center" style="top:22px;font-size:8px">QNV Dominicana</div>
  <svg class="swoosh" height="40" viewBox="0 0 100 20" preserveAspectRatio="none"><path d="M0,6 Q50,0 100,8 L100,20 L0,20Z" fill="var(--orange)"/><path d="M0,9 Q50,3 100,11 L100,20 L0,20Z" fill="var(--teal)"/></svg>
  <div class="cd-hole"></div>
</div>

<div class="piece sleeve">
  <div class="brand center" style="top:80px;font-size:14px">QNV Dominicana</div>
  <svg class="swoosh" height="60" viewBox="0 0 100 20" preserveAspectRatio="none"><path d="M0,6 Q50,0 100,8 L100,20 L0,20Z" fill="var(--orange)"/><path d="M0,9 Q50,3 100,11 L100,20 L0,20Z" fill="var(--teal)"/></svg>
</div>

<div class="piece fax">
  <div class="brand" style="position:absolute;left:18px;top:12px;font-size:10px">QNV Dominicana</div>
  <div class="tiny addr" style="right:16px;top:10px">C/Ramon Ferrel #27<br>Tel. 809-555-0147<br>www.qnv.com.do</div>
  <h2>Fax</h2>
  <div class="fax-grid">
    <span>To:</span><span>From:</span>
    <span>Fax:</span><span>Pages:</span>
    <span>Phone:</span><span>Date:</span>
    <span>Re:</span><span>CC:</span>
  </div>
  <div class="fax-checks"><span>Urgent</span><span>For Review</span><span>Please Comment</span><span>Please Reply</span><span>Please Recycle</span></div>
  <div class="fax-rule"></div>
  <svg class="swoosh" height="22" viewBox="0 0 100 20" preserveAspectRatio="none"><path d="M0,8 Q50,0 100,6 L100,20 L0,20Z" fill="var(--orange)"/><path d="M0,11 Q50,4 100,9 L100,20 L0,20Z" fill="var(--teal)"/></svg>
</div>
</body>
</html>
```